I need a business card design for my new clinic (SPORTS MEDICINE OF KNEE). I am orthopedist, expert in sports surgery, especially knee surgery. I prefer, as colors, the colors of my logo (green, black and white). I already have my logo and should appear on my card. It's good to see my site to have ideas (www.drlucianovarela.com)
It needs contain:
my name: Dr. Luciano Varela
my registration: CRM 584-902
my specialty: Cirurgia do Joelho / Esporte
my address: Centro Executivo - Pinheiral Plaza
Av. Doutor Augusto Brandão Cunha, 2740 sala 0836
Jd. Ipanema - Ribeirão Preto - SP
my phone number: Tel (16) 8245-3908
my clinic phone: (16) 3670-4851
my e-mail: drlucianovarela@mailbox-exemplo.com
my site: www.drlucianovarela.com

Target Market(s)

futures patients

Industry/Entity Type

Clinic

Requirements
Nice to have
• letters not overfilled
straight lines, with few curves

```html
<!DOCTYPE html>
<html lang="pt-BR">
<head>
<meta charset="utf-8">
<title>Varela Traumatologia Esportiva – Cartão de visita</title>
<link rel="stylesheet" href="https://fonts.googleapis.com/css2?family=Libre+Baskerville:wght@400;700&family=Lato:wght@300;400&display=swap">
<style>
  :root{
    --green:#33925d;
    --ink:#1c1c1c;
    --paper:#e7e7e7;
    --white:#ffffff;
    --muted:#bdbdbd;
    --backdrop:#d9d6d1;
  }
  *{margin:0;padding:0;box-sizing:border-box}
  html,body{width:1200px;height:900px;overflow:hidden;background:var(--backdrop)}
  .sheet{position:relative;width:1200px;height:900px}
  .card{position:absolute;top:300px;width:540px;height:300px;overflow:hidden;box-shadow:0 6px 18px rgba(0,0,0,.25)}
  .card--front{left:40px;background:var(--green)}
  .card--back{left:620px;background:var(--paper)}

  /* front */
  .front-brand{position:absolute;right:34px;top:86px;text-align:right}
  .brand-name{font-family:"Libre Baskerville",serif;font-weight:400;color:var(--ink);font-size:64px;line-height:1;letter-spacing:1px}
  .front-tagline{font-family:"Libre Baskerville",serif;color:var(--white);font-size:17px;letter-spacing:2.5px;margin-top:6px}
  .front-site{font-family:"Libre Baskerville",serif;color:var(--white);font-size:12px;letter-spacing:4px;margin-top:8px}

  /* back */
  .back-shape{position:absolute;inset:0}
  .crm{position:absolute;right:22px;top:22px;font-family:"Lato",sans-serif;font-size:11px;color:var(--ink)}
  .back-brand{position:absolute;left:22px;top:66px;display:flex;align-items:center;gap:12px}
  .brand-square{width:58px;height:58px;background:var(--ink);border-radius:6px}
  .back-brand .brand-name{font-size:44px}
  .back-tagline{font-family:"Libre Baskerville",serif;color:var(--green);font-size:12.5px;letter-spacing:1.4px;margin-top:3px}
  .doctor{position:absolute;left:24px;top:204px;font-family:"Lato",sans-serif;color:var(--white)}
  .doctor-name{font-size:19px;font-weight:400;letter-spacing:.5px;line-height:1.1}
  .doctor-specialty{font-size:11px;color:var(--muted);letter-spacing:.6px;margin-top:2px}
  .contacts{position:absolute;left:24px;top:248px;list-style:none;font-family:"Lato",sans-serif;color:var(--white);font-size:12px;font-weight:300}
  .contacts li{display:flex;align-items:center;gap:8px;height:14px}
  .contacts svg{width:10px;height:10px;fill:var(--green)}
  .address{position:absolute;right:22px;top:172px;text-align:right;font-family:"Lato",sans-serif;font-style:normal;font-size:10px;line-height:1.5;color:var(--muted)}
</style>
</head>
<body>
<main class="sheet">

  <section class="card card--front" aria-label="Frente do cartão">
    <div class="front-brand">
      <div class="brand-name">VARELA</div>
      <div class="front-tagline">Traumatologia Esportiva</div>
      <div class="front-site">www.drlucianovarela.com</div>
    </div>
  </section>

  <section class="card card--back" aria-label="Verso do cartão">
    <svg class="back-shape" width="540" height="300" viewBox="0 0 540 300" aria-hidden="true">
      <defs>
        <linearGradient id="charcoalFade" x1="0" y1="1" x2="1" y2="0">
          <stop offset="0" stop-color="#4a4a4a"/>
          <stop offset="1" stop-color="#262626"/>
        </linearGradient>
      </defs>
      <path d="M0 192 C280 188 440 140 540 40 L540 300 L0 300 Z" fill="url(#charcoalFade)"/>
      <path d="M0 182 C280 178 440 130 540 30 L540 36 C440 138 280 188 0 194 Z" fill="#33925d"/>
    </svg>

    <div class="crm">CRM 584-902</div>

    <div class="back-brand">
      <div class="brand-square"></div>
      <div>
        <div class="brand-name">VARELA</div>
        <div class="back-tagline">Traumatologia Esportiva</div>
      </div>
    </div>

    <div class="doctor">
      <div class="doctor-name">DR. LUCIANO VARELA</div>
      <div class="doctor-specialty">CIRURGIA DO JOELHO / ESPORTE</div>
    </div>

    <ul class="contacts">
      <li><svg viewBox="0 0 10 10"><rect x="2" y="0" width="6" height="10" rx="1"/></svg>(16) 8245-3908</li>
      <li><svg viewBox="0 0 10 10"><path d="M1 1 L4 1 L4 3 L3 4 Q4 6 6 7 L7 6 L9 6 L9 9 Q4 9 1 4 Z"/></svg>(16) 3670-4851</li>
      <li><svg viewBox="0 0 10 10"><path d="M0 2 H10 V8 H0 Z M0 2 L5 6 L10 2"/></svg>drlucianovarela@mailbox-exemplo.com</li>
    </ul>

    <address class="address">
      Centro Executivo - Pinheiral Plaza<br>
      Av. Doutor Augusto Brandão Cunha,<br>
      2740 sala 0836 Jd. Ipanema - Ribeirão Preto - SP
    </address>
  </section>

</main>
</body>
</html>
```